Carpentry and Building Business Card

I'm looking for a business card that is minimalistic and that incorporates the theme of my Velmor logo.
On one side I'd like the VELMOR logo with my details on the other side.
Double sided with curved edges

Target Market(s)

Construction / renovation
Adults

Industry/Entity Type

Tradesman

Contact Information for Business Card

Logo on one side, details on the other

Colors

Designer to choose only greyscale colors for use in the design.

Requirements
Must have
• Nilo Petrakis
VELMOR CONSTRUCT
Carpentry & Building Services
0481236574
Velmorconstruct@brixmail.com
Lic No. 718263D
Nice to have
• Fb and insta icons. @velmorconstruct
Should not have
• No hammer or tool icons please.

No address line.

```html
<!DOCTYPE html>
<html lang="en">
<head>
<meta charset="utf-8">
<title>Velmor Construct – Business Card</title>
<link href="https://fonts.googleapis.com/css2?family=Montserrat:wght@300;400;500;600;700&display=swap" rel="stylesheet">
<style>
  :root {
    --backdrop: #232323;
    --card: #ffffff;
    --orange: #ed9940;
    --orange-light: #f7cfa3;
    --ink: #111111;
    --white: #ffffff;
  }
  * { margin: 0; padding: 0; box-sizing: border-box; }
  html, body { width: 1200px; height: 1200px; overflow: hidden; }
  body {
    background: var(--backdrop);
    font-family: "Montserrat", sans-serif;
    position: relative;
  }
  .card {
    position: absolute;
    left: 211px;
    width: 778px;
    height: 419px;
    border-radius: 34px;
    background: var(--card);
    overflow: hidden;
  }
  .card-front { top: 101px; }
  .card-back { top: 614px; }
  .card-shape { position: absolute; inset: 0; width: 100%; height: 100%; }

  .front-wordmark {
    position: absolute;
    left: 0; right: 0;
    top: 178px;
    text-align: center;
    font-size: 70px;
    font-weight: 600;
    letter-spacing: 22px;
    color: var(--ink);
    line-height: 1;
    padding-left: 22px;
  }

  .contact-list {
    position: absolute;
    left: 0;
    top: 135px;
    width: 330px;
    list-style: none;
  }
  .contact-item {
    display: flex;
    justify-content: flex-end;
    align-items: center;
    height: 28px;
    margin-bottom: 10.5px;
  }
  .contact-text {
    font-size: 15px;
    font-weight: 500;
    color: var(--ink);
    margin-right: 26px;
    white-space: nowrap;
  }
  .contact-icon {
    width: 28px;
    height: 28px;
    background: var(--orange);
    display: flex;
    align-items: center;
    justify-content: center;
  }
  .contact-icon svg { width: 16px; height: 16px; }

  .brand-block {
    position: absolute;
    left: 442px;
    width: 295px;
    top: 84px;
    text-align: right;
    color: var(--white);
  }
  .back-wordmark {
    font-size: 38px;
    font-weight: 500;
    letter-spacing: 10px;
    line-height: 1;
    margin-right: -10px;
    padding-top: 14px;
    height: 70px;
  }
  .brand-rule {
    border: 0;
    border-top: 1px solid var(--white);
    margin-top: 16px;
    margin-left: -1px;
  }
  .brand-name {
    font-size: 16px;
    font-weight: 700;
    margin-top: 9px;
    line-height: 1.2;
  }
  .brand-tagline {
    font-size: 16px;
    font-weight: 300;
    margin-top: 4px;
    line-height: 1.2;
  }
  .social-list { list-style: none; margin-top: 14px; }
  .social-item {
    display: flex;
    justify-content: flex-end;
    align-items: center;
    height: 35px;
    margin-bottom: 11px;
  }
  .social-handle { font-size: 13px; font-weight: 600; margin-right: 14px; }
  .social-dot {
    width: 35px; height: 35px;
    border-radius: 50%;
    background: var(--white);
  }
</style>
</head>
<body>

<section class="card card-front" aria-label="Front of card">
  <svg class="card-shape" viewBox="0 0 972 524" preserveAspectRatio="none" aria-hidden="true">
    <path fill="var(--orange-light)" d="M0,428 C160,478 360,492 560,418 C700,366 760,300 830,298 C900,296 920,360 972,388 L972,524 L0,524 Z"/>
    <path fill="var(--orange)" d="M0,443 C160,490 360,504 565,430 C705,378 765,312 830,311 C895,310 920,375 972,402 L972,524 L0,524 Z"/>
  </svg>
  <div class="front-wordmark">VELMOR.</div>
</section>

<section class="card card-back" aria-label="Back of card">
  <svg class="card-shape" viewBox="0 0 972 524" preserveAspectRatio="none" aria-hidden="true">
    <circle cx="852" cy="252" r="410" fill="var(--orange-light)"/>
    <circle cx="852" cy="252" r="398" fill="var(--orange)"/>
  </svg>

  <ul class="contact-list">
    <li class="contact-item">
      <span class="contact-text">Nilo Petrakis</span>
      <span class="contact-icon"><svg viewBox="0 0 16 16" fill="none" stroke="#fff" stroke-width="1"><circle cx="8" cy="5" r="3"/><path d="M2.5 14c0-3 2.5-5 5.5-5s5.5 2 5.5 5z"/></svg></span>
    </li>
    <li class="contact-item">
      <span class="contact-text">0481236574</span>
      <span class="contact-icon"><svg viewBox="0 0 16 16" fill="none" stroke="#fff" stroke-width="1"><path d="M1.5 6c0-2 3-3 6.5-3s6.5 1 6.5 3v1h-3V5.5h-7V7h-3z"/><path d="M4 8l-1 5h10l-1-5z"/><circle cx="8" cy="10.5" r="1.3"/></svg></span>
    </li>
    <li class="contact-item">
      <span class="contact-text">Velmorconstruct@brixmail.com</span>
      <span class="contact-icon"><svg viewBox="0 0 16 16" fill="none" stroke="#fff" stroke-width="1"><rect x="2" y="4" width="12" height="8"/><path d="M2 4l6 5 6-5"/></svg></span>
    </li>
    <li class="contact-item">
      <span class="contact-text">Lic No. 718263D</span>
      <span class="contact-icon"><svg viewBox="0 0 16 16" fill="none" stroke="#fff" stroke-width="1"><rect x="1.5" y="3" width="13" height="10"/><path d="M3.5 6h5M3.5 8h5M3.5 10h5"/><rect x="10" y="5.5" width="3" height="4"/></svg></span>
    </li>
  </ul>

  <div class="brand-block">
    <div class="back-wordmark">VELMOR.</div>
    <hr class="brand-rule">
    <p class="brand-name">CONSTRUCT</p>
    <p class="brand-tagline">Carpentry &amp; Building Services</p>
    <ul class="social-list">
      <li class="social-item"><span class="social-handle">@velmorconstruct</span><span class="social-dot"></span></li>
      <li class="social-item"><span class="social-handle">@velmorconstruct</span><span class="social-dot"></span></li>
    </ul>
  </div>
</section>

</body>
</html>
```